Electrical contractor in San Diego county since 1988

Provide a company name/ logo for business cards and forms. Newer and more modern old card is attached. Color preference is black and orange. Simple and streamlined nothing too busy. I have also attached a card that represents the simplicity of what we are looking for.

Contractor

```html
<!DOCTYPE html>
<html lang="en">
<head>
<meta charset="utf-8">
<title>K.M. Electric Inc. – Business Card</title>
<link rel="stylesheet" href="https://fonts.googleapis.com/css2?family=Lato:wght@400;700;900&display=swap">
<style>
  :root {
    --stage: #262626;
    --card: #ffffff;
    --band: #2b2a28;
    --accent: #f5b70f;
    --ink: #1f1f1f;
    --muted: #555555;
  }
  html, body {
    margin: 0;
    width: 1200px;
    height: 900px;
    overflow: hidden;
    background: var(--stage);
    font-family: "Lato", Arial, sans-serif;
  }
  .card {
    position: absolute;
    left: 180px;
    top: 210px;
    width: 840px;
    height: 480px;
    background: var(--card);
    clip-path: polygon(0 0, 100% 0, 100% 100%, 0 100%, 0 56%, 5% 50%, 5% 45%, 0 39%);
  }
  .brand {
    position: absolute;
    left: 52px;
    top: 38px;
  }
  .brand-name {
    margin: 0;
    font-size: 32px;
    font-weight: 900;
    color: var(--accent);
    line-height: 1;
  }
  .brand-tagline {
    margin: 6px 0 0;
    font-size: 16px;
    font-weight: 700;
    color: var(--ink);
  }
  .brand-license {
    margin: 2px 0 0;
    font-size: 15px;
    color: var(--muted);
  }
  .person {
    position: absolute;
    left: 110px;
    top: 168px;
  }
  .person-name {
    margin: 0;
    font-size: 25px;
    font-weight: 900;
    color: var(--ink);
    letter-spacing: 0.3px;
  }
  .person-title {
    margin: 0;
    font-size: 17px;
    color: var(--accent);
  }
  .contact {
    position: absolute;
    display: grid;
    grid-template-columns: 20px auto;
    column-gap: 10px;
    row-gap: 2px;
    align-items: center;
    font-size: 19px;
    color: var(--ink);
    letter-spacing: 0.4px;
  }
  .contact svg { width: 18px; height: 18px; fill: var(--accent); }
  .contact-phones { left: 110px; top: 330px; }
  .contact-address { left: 400px; top: 360px; align-items: start; }
  .contact-address svg { width: 20px; height: 24px; margin-top: 2px; }
  .band {
    position: absolute;
    right: 0;
    top: 0;
    width: 170px;
    height: 100%;
    background: var(--band);
    border-left: 7px solid var(--accent);
  }
  .band-name {
    position: absolute;
    left: 50%;
    top: 50%;
    margin: 0;
    transform: translate(-50%, -50%) rotate(90deg);
    white-space: nowrap;
    font-size: 46px;
    font-weight: 900;
    color: var(--accent);
  }
</style>
</head>
<body>
  <main class="card">
    <header class="brand">
      <h1 class="brand-name">K.M. Electric Inc.</h1>
      <p class="brand-tagline">Commercial - New &amp; Remodel</p>
      <p class="brand-license">Lic. 730218</p>
    </header>

    <section class="person">
      <h2 class="person-name">DALTON REESE</h2>
      <p class="person-title">President</p>
    </section>

    <section class="contact contact-phones">
      <svg viewBox="0 0 24 24" aria-label="Phone"><path d="M2 8c0-3 4-5 10-5s10 2 10 5v2h-5V8c-2-1-8-1-10 0v2H2zM6 11h12l3 9H3z"/></svg>
      <span>(619) 555-0142</span>
      <svg viewBox="0 0 24 24" aria-label="Fax"><path d="M6 2h12v6H6zM2 9h20v9h-4v-3H6v3H2zM7 16h10v6H7z"/></svg>
      <span>(619) 555-0178</span>
    </section>

    <section class="contact contact-address">
      <svg viewBox="0 0 20 24" aria-label="Address"><path d="M10 0a9 9 0 0 0-9 9c0 6 9 15 9 15s9-9 9-15a9 9 0 0 0-9-9zm0 13a4 4 0 1 1 0-8 4 4 0 0 1 0 8z"/></svg>
      <span>P.O. Box 2417<br>Alpine, CA 91901-0417</span>
    </section>

    <aside class="band">
      <p class="band-name">K.M. Electric Inc.</p>
    </aside>
  </main>
</body>
</html>
```